Criminal Defense Law Firm needs Stationary design Theme for a Business Card, Envelope, and Letterhea

Our Law Firm is seeking a general design concept for a business card, letterhead, and Envelope.

Our website is WillowcrestTrialDesk.com

A design for these three items is requested to keep branding in place for the firm. Would like to keep the Firm Colors on the website consistent with our branding on business cards, letterheads, and mailing envelopes #10 size to be exact.

We would like business cards printed front and back with Law firm Colors from website.

Letterhead with law firm colors as well. Design is not limited to just the header, but the footer can be utilized as well for email, website, phone, fax, etc.

Simple #10 envelope consisting of the same design principles set out in the previous two designs.

```html
<!DOCTYPE html>
<html lang="en">
<head>
<meta charset="utf-8">
<title>Willowcrest Trial Desk — Stationery</title>
<link href="https://fonts.googleapis.com/css2?family=Bitter:wght@400;600&family=Arimo:wght@400&family=PT+Sans&display=swap" rel="stylesheet">
<style>
:root{
  --stage:#5b3a22;
  --paper:#ffffff;
  --ink:#1f2321;
  --band:#1e2220;
  --band-line:#6b6b6b;
  --flap-grey:#606060;
  --rule:#333;
  --light:#e6e6e6;
}
*{margin:0;padding:0;box-sizing:border-box}
html,body{width:1200px;height:553px;overflow:hidden;background:var(--stage)}
.canvas{position:relative;width:1200px;height:553px}
.sheet{position:absolute;background:var(--paper);box-shadow:0 1px 3px rgba(0,0,0,.35)}
.serif{font-family:"Bitter",Georgia,serif}
.brand{position:absolute;display:flex;align-items:flex-start;gap:6px}
.brand-mark{border:1.5px solid var(--ink);border-radius:50%;flex:none}
.brand-name{font-family:"Bitter",Georgia,serif;font-weight:600;color:var(--ink);line-height:1.05;text-transform:uppercase}
.brand-url{font-family:"Bitter",Georgia,serif;font-size:8.5px;color:var(--ink);position:absolute}
.footer-band{position:absolute;left:0;right:0;bottom:0;height:30px;background:var(--band);border-top:3px solid var(--band-line);display:flex;align-items:center;justify-content:center;gap:12px;color:#e6e6e6;font-family:"Bitter",Georgia,serif;font-size:7px;line-height:1.3}
.footer-band .dot{width:20px;height:20px;border:1px solid #888;border-radius:50%}
.contact-left{text-align:left}
.fax-title{position:absolute;left:17px;top:98px;font-family:"Arimo",Arial,sans-serif;font-size:22px;color:var(--ink)}
.fax-field{position:absolute;font-family:"Arimo",Arial,sans-serif;font-size:5.5px;color:var(--ink);border-bottom:1px solid var(--rule);height:9px;width:115px}
.fax-field.left{left:17px;width:155px}
.fax-field.right{left:186px}
.fax-checks{position:absolute;left:17px;top:219px;display:flex;gap:14px;font-family:"Arimo",Arial,sans-serif;font-size:5.8px;color:var(--ink)}
.fax-checks span::before{content:"";display:inline-block;width:7px;height:7px;border:0.8px solid var(--ink);margin-right:4px;vertical-align:-1px}
.envelope{position:absolute;background:var(--paper);border:1px solid #ccc;overflow:hidden}
.envelope .flap{position:absolute;left:0;top:0;width:100%}
.envelope .flap-dot{position:absolute;border:1px solid rgba(255,255,255,.35);border-radius:50%}
.front-env{background:linear-gradient(135deg,#fff 40%,#e4e4e4)}
.env-band{position:absolute;left:0;right:0;bottom:0;height:19px;background:var(--band);border-top:3px solid #bbb;display:flex;align-items:center;gap:20px;padding-left:6px;font-family:"Bitter",Georgia,serif;font-size:7.5px;color:#ddd}
.env-band .dot{width:13px;height:13px;border:1px solid #888;border-radius:50%}
.card{position:absolute;background:var(--paper);overflow:hidden}
.card-name{position:absolute;font-family:"Bitter",Georgia,serif;font-size:4.6px;color:var(--ink);line-height:1.25;text-align:right}
.card-name b{font-size:5.2px;font-weight:600}
.card-info{position:absolute;font-family:"Bitter",Georgia,serif;font-size:3.9px;color:var(--ink);line-height:1.4;border-left:0.6px solid var(--ink);padding-left:3px}
.card-band{position:absolute;left:0;right:0;bottom:0;height:9px;background:var(--band);border-top:1.5px solid #999;font-family:"Bitter",Georgia,serif;font-size:3px;color:#bbb;display:flex;align-items:center;padding-left:4px}
.card-back{background:var(--band);display:flex;flex-direction:column;align-items:center;justify-content:flex-end;padding-bottom:10px}
.card-back .ghost{width:26px;height:26px;border:1px solid #3a3f3c;border-radius:50%;margin-bottom:8px}
.card-back .name{font-family:"Bitter",Georgia,serif;font-size:9px;color:#e8e8e8;text-align:center;line-height:1.3}
.option-label{position:absolute;top:500px;font-family:"PT Sans",Arial,sans-serif;font-size:26px;color:#fff;transform:translateX(-50%)}
</style>
</head>
<body>
<main class="canvas">

  <!-- Letterhead, option 1 -->
  <section class="sheet letterhead" style="left:26px;top:50px;width:336px;height:434px">
    <div class="brand" style="left:81px;top:12px">
      <span class="brand-mark" style="width:25px;height:25px"></span>
      <span class="brand-name" style="font-size:10px">Willowcrest Trial<br>Desk</span>
    </div>
    <span class="brand-url" style="left:118px;top:38px">www.willowcresttrialdesk.com</span>
    <footer class="footer-band">
      <div class="contact-left">&#9990; 505.555.0142 &nbsp;&#9990; 505.555.0187<br>&#9993; willowcresttrialdesk@mail.com</div>
      <span class="dot"></span>
      <div class="contact-left">2214 Alder Lane NW, Fernhaven<br>NM 87000</div>
    </footer>
  </section>

  <!-- Fax sheet, option 2 -->
  <section class="sheet fax-sheet" style="left:381px;top:50px;width:335px;height:434px">
    <div class="brand" style="left:16px;top:16px">
      <span class="brand-mark" style="width:25px;height:25px"></span>
      <span class="brand-name" style="font-size:10px">Willowcrest Trial<br>Desk</span>
    </div>
    <span class="brand-url" style="left:16px;top:44px">www.willowcresttrialdesk.com</span>
    <h1 class="fax-title" style="font-weight:400">FAX</h1>
    <div class="fax-field left" style="top:136px">To :</div>
    <div class="fax-field right" style="top:136px">From :</div>
    <div class="fax-field left" style="top:154px">Fax :</div>
    <div class="fax-field right" style="top:154px">Pages :</div>
    <div class="fax-field left" style="top:171px">Phone :</div>
    <div class="fax-field right" style="top:171px">Date :</div>
    <div class="fax-field left" style="top:189px">Re :</div>
    <div class="fax-field right" style="top:189px">CC :</div>
    <div class="fax-checks">
      <span>Urgent</span><span>For Review</span><span>Please Comment</span><span>Please Reply</span><span>Please Recycle</span>
    </div>
    <footer class="footer-band">
      <div class="contact-left">&#9990; 505.555.0142 &nbsp;&#9990; 505.555.0187<br>&#9993; willowcresttrialdesk@mail.com</div>
      <span class="dot"></span>
      <div class="contact-left">2214 Alder Lane NW, Fernhaven<br>NM 87000</div>
    </footer>
  </section>

  <!-- Envelope backs -->
  <section class="envelope" style="left:806px;top:43px;width:374px;height:167px">
    <svg class="flap" width="374" height="70" viewBox="0 0 374 70"><polygon points="0,0 374,0 374,20 210,65 164,65 0,20" fill="var(--flap-grey)"/></svg>
    <span class="flap-dot" style="left:172px;top:10px;width:30px;height:30px;border-color:#3c3c3c"></span>
  </section>
  <section class="envelope" style="left:794px;top:117px;width:374px;height:167px">
    <svg class="flap" width="374" height="70" viewBox="0 0 374 70"><polygon points="0,0 374,0 374,20 210,67 164,67 0,20" fill="var(--band)"/></svg>
    <span class="flap-dot" style="left:172px;top:12px;width:30px;height:30px"></span>
  </section>

  <!-- Envelope front -->
  <section class="envelope front-env" style="left:768px;top:200px;width:374px;height:170px">
    <div class="brand" style="left:3px;top:10px">
      <span class="brand-mark" style="width:22px;height:22px"></span>
      <span class="brand-name" style="font-size:7.5px">Willowcrest Trial<br>Desk</span>
    </div>
    <footer class="env-band">
      <span>2214 Alder Lane NW, Fernhaven, NM 87000</span>
      <span class="dot"></span>
      <span>&#9679; www.willowcresttrialdesk.com</span>
    </footer>
  </section>

  <!-- Business card front, variant A -->
  <section class="card" style="left:740px;top:394px;width:126px;height:80px">
    <div class="brand" style="left:27px;top:4px;gap:4px">
      <span class="brand-mark" style="width:13px;height:13px;border-width:1px"></span>
      <span class="brand-name" style="font-size:5px">Willowcrest Trial<br>Desk</span>
    </div>
    <div class="card-name" style="right:64px;top:36px"><b>Owen Valdera</b><br>Designation<br><br>2214 Alder Lane NW,<br>Fernhaven, NM 87000</div>
    <div class="card-info" style="left:64px;top:35px">&#9990; 505.555.0142<br>&#9990; 505.555.0187<br>&#9993; willowcresttrialdesk@mail.com<br>&#9679; www.willowcresttrialdesk.com</div>
    <footer class="card-band" style="justify-content:center;padding-left:0"><span style="width:7px;height:7px;border:0.6px solid #777;border-radius:50%"></span></footer>
  </section>

  <!-- Business card front, variant B -->
  <section class="card" style="left:878px;top:394px;width:145px;height:80px">
    <div class="brand" style="left:10px;top:4px;gap:4px">
      <span class="brand-mark" style="width:13px;height:13px;border-width:1px"></span>
      <span class="brand-name" style="font-size:5px">Willowcrest Trial<br>Desk</span>
    </div>
    <div class="card-name" style="left:10px;top:36px;text-align:left"><b>Owen Valdera</b><br>Designation<br><br>2214 Alder Lane NW,<br>Fernhaven, NM 87000</div>
    <div class="card-info" style="left:54px;top:35px">&#9990; 505.555.0142<br>&#9990; 505.555.0187<br>&#9993; willowcresttrialdesk@mail.com<br>&#9679; www.willowcresttrialdesk.com</div>
    <footer class="card-band">We Are Here To Guide You Through Every Step Of The Legal Process.</footer>
  </section>

  <!-- Business card back -->
  <section class="card card-back" style="left:1031px;top:394px;width:139px;height:79px">
    <span class="ghost"></span>
    <div class="name">WILLOWCREST TRIAL<br>DESK</div>
  </section>

  <p class="option-label" style="left:190px">Option-1</p>
  <p class="option-label" style="left:594px">Option-2</p>
</main>
</body>
</html>
```